MEDITERRANEAN Cafe Website needed

We are a MEDITERRANEAN Café serving Coffee, breakfast, Pizza, Pasta, Sandwiches etc.

We need a home page, menu & venue, Reservations & Events, Delivery
Connect (Social media / Feedback / Contact us),Join our team
Updates

Can we keep the designs in Mediterranean colours, look, and feel pleasethanks Added Saturday, December 10, 2016

Project Deadline Extended Reason: I have guarantied the payment and upgraded the project. I would like this would to give more time for new designs to come in and a couple of potential designs to show more. Added Sunday, December 11, 2016

Industry/Entity Type

Cafe

Coding

Coded - Design and coding required

Number of Pages Required

5+ page

Requirements
Must have
• MEDITERRANEAN feel, colours, style etc.
• http://www.corvanetta (DOT) co (DOT) uk
Nice to have

```html
<!DOCTYPE html>
<html lang="en">
<head>
<meta charset="utf-8">
<title>Lirana Café — Mediterranean Café</title>
<link rel="stylesheet" href="https://fonts.googleapis.com/css2?family=Lobster&family=Quicksand:wght@400;500;700&display=swap">
<style>
:root{
  --accent:#f0553a;
  --accent-soft:#f57a5c;
  --blue:#4a5fe6;
  --ink:#333;
  --muted:#666;
  --grey-bg:#f2f2f2;
  --white:#fff;
  --wood:#2f2520;
  --script:"Lobster", cursive;
  --sans:"Quicksand", sans-serif;
}
*{box-sizing:border-box;margin:0;padding:0}
html,body{width:1200px;height:4337px;overflow:hidden}
body{position:relative;font-family:var(--sans);color:var(--ink);background:var(--white)}
.abs{position:absolute}
.script{font-family:var(--script);font-weight:400}
.btn{position:absolute;display:flex;align-items:center;justify-content:center;font-family:var(--sans);font-weight:500;font-size:14px;letter-spacing:1px;text-transform:uppercase;border-radius:30px}
.btn-solid{background:var(--accent);color:var(--white)}
.btn-outline{border:2px solid var(--accent-soft);color:var(--accent)}
.btn-ghost{border:2px solid rgba(255,255,255,.8);color:var(--white)}

/* header */
.site-header{position:absolute;left:0;top:0;width:1200px;height:84px;background:rgba(255,255,255,.82);z-index:5}
.brand{position:absolute;left:40px;top:10px;display:flex;align-items:center;gap:14px}
.brand-dot{width:58px;height:58px;border-radius:50%;background:var(--blue)}
.brand-name{font-family:var(--script);font-size:34px;color:var(--blue)}
.main-nav{position:absolute;right:285px;top:32px;display:flex;gap:30px;font-size:15px;font-weight:500;text-transform:uppercase;color:#444}
.main-nav .current{color:var(--blue)}
.site-header .btn{right:40px;top:18px;width:136px;height:48px;font-size:13px}

/* hero */
.hero{left:0;top:0;width:1200px;height:660px;background:linear-gradient(100deg,#c9a3b8 0%,#e48a8a 40%,#f0a27a 100%)}
.hero-title{left:40px;top:240px;font-size:50px;color:var(--white)}
.hero-sub{left:40px;top:318px;font-size:30px;color:var(--white);line-height:1.35}
.hero-sub b{font-family:var(--script);font-weight:400;font-size:50px}
.hero .btn{left:40px;top:442px;width:136px;height:50px}
.dots{left:570px;top:580px;display:flex;gap:10px}
.dots i{width:14px;height:14px;border-radius:50%;border:2px solid #fff;display:block}
.dots i.on{background:#fff}

/* menu cards */
.menu-band{left:0;top:636px;width:1200px;height:483px;background:var(--grey-bg)}
.card{position:absolute;top:6px;width:358px;height:416px;background:var(--white);box-shadow:0 2px 8px rgba(0,0,0,.08)}
.card h2{font-family:var(--script);font-weight:400;font-size:38px;text-align:center;padding-top:18px;height:87px;color:#333}
.card .photo{width:100%;height:219px}
.card .btn{left:104px;top:354px;width:150px;height:48px;font-size:13px}

/* about */
.about{left:0;top:1119px;width:1200px;height:517px;background:linear-gradient(120deg,#8e6f9a 0%,#a06e8e 50%,#b9786f 100%)}
.about h2{position:absolute;left:0;width:1200px;top:60px;text-align:center;font-size:48px;color:var(--white)}
.divider{position:absolute;display:flex;align-items:center;gap:14px}
.divider span{display:block;height:1px;width:220px;background:currentColor;opacity:.5}
.about p{position:absolute;left:240px;top:200px;width:720px;text-align:center;color:var(--white);font-size:16px;line-height:1.85}
.about .btn{left:534px;top:380px;width:132px;height:48px;font-size:13px}

/* chef selection */
.chef h2{position:absolute;left:0;width:1200px;top:1678px;text-align:center;font-size:48px;color:var(--accent)}
.dish{position:absolute}
.dish .label{position:absolute;left:0;bottom:0;width:100%;height:64px;background:rgba(240,100,70,.82);display:flex;align-items:center;justify-content:center;font-family:var(--script);font-size:32px;color:var(--white)}

/* booking */
.booking{left:0;top:2590px;width:1200px;height:709px;background:linear-gradient(90deg,#2b211c 0%,#3a2c24 55%,#4a342a 100%)}
.booking .pizza{position:absolute;right:0;top:60px;width:330px;height:600px;background:radial-gradient(ellipse at 60% 50%,#d9893f 0%,#b65a2b 55%,rgba(74,52,42,0) 78%)}
.booking h2{position:absolute;left:0;width:1200px;top:52px;text-align:center;font-size:36px;color:var(--white)}
.field{position:absolute;height:56px;border:1px solid rgba(255,255,255,.55);color:var(--white);font-size:15px;font-weight:500;text-transform:uppercase;padding:16px 14px}
.field.message{height:136px}
.booking .btn{left:520px;top:590px;width:190px;height:48px;font-size:13px}

/* contacts */
.contacts h2{position:absolute;left:0;width:1200px;top:3368px;text-align:center;font-size:36px;color:#333}
.contact-col{position:absolute;top:3540px;width:360px;text-align:center;font-size:15px;line-height:1.6;color:var(--muted)}
.contact-col svg{display:block;margin:0 auto 22px}
.socials{display:flex;justify-content:center;gap:12px}
.socials i{display:block;width:36px;height:36px;border-radius:50%;border:1.5px solid #bbb}

/* map + hours */
.map{left:0;top:3724px;width:1200px;height:555px;background:linear-gradient(135deg,#dfe8d8 0%,#cfe2ee 45%,#7fc1ea 75%,#5ab0e6 100%)}
.hours{position:absolute;left:40px;top:63px;width:330px;height:289px;background:rgba(255,255,255,.88);padding:28px 26px;font-size:15px;line-height:1.55;color:#444}
.hours h3{display:flex;align-items:center;gap:12px;font-size:22px;font-weight:500;color:var(--blue);text-transform:uppercase;margin-bottom:14px}
.hours b{font-weight:700;color:#333}

.site-footer{left:0;top:4279px;width:1200px;height:58px;background:var(--blue);color:var(--white);font-size:13px;letter-spacing:1px;display:flex;align-items:center;justify-content:center;text-transform:uppercase}
</style>
</head>
<body>

<header class="site-header">
  <div class="brand"><span class="brand-dot"></span><span class="brand-name">Lirana</span></div>
  <nav class="main-nav">
    <span class="current">Homepage</span><span>Menu</span><span>Location</span><span>Events</span><span>Delivery</span><span>Join Team</span>
  </nav>
  <span class="btn btn-solid">Book a Table</span>
</header>

<section class="hero abs" role="img" aria-label="Waffle topped with fresh berries under a warm pink-orange overlay">
  <h1 class="hero-title abs script">Happy Hour Discounts</h1>
  <p class="hero-sub abs">Specials Breakfast Happy Hour<br>for <b>10%</b> Discount</p>
  <span class="btn btn-ghost">View Menu</span>
  <div class="dots abs"><i></i><i></i><i class="on"></i></div>
</section>

<section class="menu-band abs">
  <article class="card" style="left:40px">
    <h2>Food</h2>
    <div class="photo" role="img" aria-label="Grilled salmon with tomatoes and greens" style="background:linear-gradient(135deg,#e9ded3,#d86a45 55%,#7a9a5a)"></div>
    <span class="btn btn-outline">View Menu</span>
  </article>
  <article class="card" style="left:421px">
    <h2>Desserts</h2>
    <div class="photo" role="img" aria-label="Chocolate cake with cream on a plate" style="background:linear-gradient(135deg,#e6e2dd,#7a4a30 55%,#c9bfb5)"></div>
    <span class="btn btn-outline">View Menu</span>
  </article>
  <article class="card" style="left:801px">
    <h2>Drinks</h2>
    <div class="photo" role="img" aria-label="Lime lemonade glasses with straws" style="background:linear-gradient(135deg,#d6e89a,#9cc83c 50%,#e8f0c8)"></div>
    <span class="btn btn-outline">View Menu</span>
  </article>
</section>

<section class="about abs" role="img" aria-label="Close-up of a pizza under a violet overlay">
  <h2 class="script">About Us</h2>
  <div class="divider" style="left:375px;top:140px;color:#fff"><span></span>
    <svg width="24" height="24" viewBox="0 0 24 24" fill="none" stroke="#fff" stroke-width="1.5"><path d="M6 4v16M4 4v5a2 2 0 0 0 4 0V4M17 4c-2 0-3 3-3 6s1 4 3 4v6"/></svg><span></span></div>
  <p>With influences from the Mediterranean, Lirana Café was founded with a great deal of intuition into what makes a dining experience great. Lirana Café is a place where people come to chat, meet up or even work. We set out to offer our guests an experience they wouldn't soon forget and an inventive menu selection all made fresh with quality ingredients and served in a warm and casually comfortable setting.</p>
  <span class="btn btn-solid">Book a Table</span>
</section>

<section class="chef">
  <h2 class="script">Chef Selection</h2>
  <div class="divider" style="left:375px;top:1770px;color:#7a8ad8"><span></span>
    <svg width="24" height="24" viewBox="0 0 24 24" fill="none" stroke="#7a8ad8" stroke-width="1.5"><path d="M6 4v16M4 4v5a2 2 0 0 0 4 0V4M17 4c-2 0-3 3-3 6s1 4 3 4v6"/></svg><span></span></div>

  <div class="dish" style="left:40px;top:1845px;width:550px;height:315px;background:linear-gradient(135deg,#eee,#9aa35a 50%,#ddd)" role="img" aria-label="Pesto pasta on a white plate"><span class="label">Pasta Pesto</span></div>
  <div class="dish" style="left:610px;top:1845px;width:263px;height:315px;background:linear-gradient(135deg,#e8e0d4,#e9c27a 55%,#c4502e)" role="img" aria-label="Bowl of hummus with paprika"><span class="label">Hummus</span></div>
  <div class="dish" style="left:893px;top:1845px;width:267px;height:315px;background:linear-gradient(135deg,#e9e6df,#c89a6a 50%,#6d8a3c)" role="img" aria-label="Grilled chicken salad"><span class="label">Hummus</span></div>
  <div class="dish" style="left:40px;top:2174px;width:264px;height:318px;background:linear-gradient(135deg,#ece8e0,#c9a074 50%,#7a9a42)" role="img" aria-label="Grilled chicken salad"><span class="label">Hummus</span></div>
  <div class="dish" style="left:327px;top:2174px;width:546px;height:318px;background:linear-gradient(135deg,#9a9894,#d8592e 45%,#e8e0cc 70%,#8c8a86)" role="img" aria-label="Shakshuka with eggs in a pan on a wooden table"><span class="label">Pasta Pesto</span></div>
  <div class="dish" style="left:896px;top:2174px;width:264px;height:318px;background:linear-gradient(135deg,#e8e3da,#c96a30 50%,#8a4020)" role="img" aria-label="Grilled meat with vegetables"><span class="label">Hummus</span></div>
</section>

<section class="booking abs">
  <div class="pizza" role="img" aria-label="Pizza slices with basil on a dark wooden table"></div>
  <h2 class="script">Book A Table Now</h2>
  <div class="field" style="left:40px;top:188px;width:550px">Name</div>
  <div class="field" style="left:610px;top:188px;width:548px">Email</div>
  <div class="field" style="left:40px;top:263px;width:550px">Telephone Number</div>
  <div class="field" style="left:610px;top:263px;width:548px">Number of Guests</div>
  <div class="field" style="left:40px;top:342px;width:550px">Date</div>
  <div class="field" style="left:610px;top:342px;width:548px">Time</div>
  <div class="field message" style="left:40px;top:420px;width:1118px">Your Message</div>
  <span class="btn btn-solid">Request a Reservation</span>
</section>

<section class="contacts">
  <h2 class="script">Contacts</h2>
  <div class="divider" style="left:375px;top:3454px;color:#999"><span></span>
    <svg width="24" height="24" viewBox="0 0 24 24" fill="none" stroke="#999" stroke-width="1.5"><path d="M6 4v16M4 4v5a2 2 0 0 0 4 0V4M17 4c-2 0-3 3-3 6s1 4 3 4v6"/></svg><span></span></div>

  <div class="contact-col" style="left:40px">
    <svg width="32" height="44" viewBox="0 0 24 32"><path d="M12 0C5.4 0 0 5.3 0 12c0 9 12 20 12 20s12-11 12-20C24 5.3 18.6 0 12 0z" fill="var(--blue)"/><circle cx="12" cy="12" r="4.5" fill="#fff"/></svg>
    18 Harbour Walk | Marina Point, Singapore<br>000000, Singapore
  </div>
  <div class="contact-col" style="left:420px">
    <svg width="44" height="34" viewBox="0 0 44 34"><rect width="44" height="34" rx="3" fill="var(--blue)"/><path d="M3 4l19 15L41 4" fill="none" stroke="#fff" stroke-width="3"/></svg>
    info@liranacafe.example<br>or reservations@liranacafe.example
  </div>
  <div class="contact-col" style="left:800px">
    <svg width="40" height="44" viewBox="0 0 40 44"><circle cx="32" cy="8" r="7" fill="var(--blue)"/><circle cx="8" cy="22" r="7" fill="var(--blue)"/><circle cx="32" cy="36" r="7" fill="var(--blue)"/><path d="M32 8L8 22l24 14" fill="none" stroke="var(--blue)" stroke-width="3"/></svg>
    <div class="socials"><i></i><i></i><i></i><i></i></div>
  </div>
</section>

<section class="map abs" role="img" aria-label="Street map of the harbour area around the café">
  <div class="hours">
    <h3><svg width="24" height="24" viewBox="0 0 24 24" fill="none" stroke="var(--blue)" stroke-width="2"><circle cx="12" cy="12" r="10"/><path d="M12 6v6l4 2"/></svg>Opening Hours</h3>
    <b>Monday - Thursday - Friday</b><br>8:30 - 3pm and 5:30pm till 10pm<br>
    <b>Tuesday - Saturday - Sunday</b><br>and public holiday 8am till 10pm<br>
    <b>Wednesday</b> - Close
  </div>
  <svg class="abs" style="left:606px;top:180px" width="32" height="44" viewBox="0 0 24 32"><path d="M12 0C5.4 0 0 5.3 0 12c0 9 12 20 12 20s12-11 12-20C24 5.3 18.6 0 12 0z" fill="#e5483a"/><circle cx="12" cy="12" r="4.5" fill="#fff"/></svg>
</section>

<footer class="site-footer abs">Lirana Café © 2015. All rights reserved</footer>

</body>
</html>
```